A wine Label for a new brand of New Zealand Wine

We are looking for a Wine Label for our "Harbor Crest" brand of wines from North Otago New Zealand. We would like the label to perhaps use the HC as a logo and the rest up to the designer. We have our vineyards located in the Waitaki Valley New Zealand which is a southern region with mountains and a river flowing past our vineyard. Photos attached of Dramatic Landscape. Also attached is a basic outline of requirements for the front bottle of the label. The rear bottle label will contain writing about the wines background plus statutory regulations on Alc. Vol, bar code etc. Front Label size to be no Larger than 80mm deep by 100 mm wide. The label can be simple or graphic, whatever the designer chooses.
Target Market(s)
New Wine Brand
Look and feel
Each slider illustrates characteristics of the customer's brand and the style your logo design should communicate.

```html
<!DOCTYPE html>
<html lang="en">
<head>
<meta charset="utf-8">
<title>Harbor Crest Pinot Gris 2015 – Front Label</title>
<link rel="stylesheet" href="https://fonts.googleapis.com/css2?family=Archivo+Black&family=Abril+Fatface&family=Open+Sans:wght@400&display=swap">
<style>
  :root {
    --page: #ffffff;
    --label-light: #f6ebe6;
    --label-edge: #ead9c8;
    --frame: #1e1a18;
    --ornament: #2a2220;
    --wordmark: #b9aa88;
    --wordmark-edge: #8e9bb0;
    --ink: #111111;
    --scene-tone: #a49c80;
  }
  html, body {
    margin: 0;
    padding: 0;
    width: 1200px;
    height: 959px;
    overflow: hidden;
    background: var(--page);
  }
  .label {
    position: relative;
    width: 1200px;
    height: 959px;
  }
  .label-shape {
    position: absolute;
    inset: 0;
  }
  .brand-name-short {
    position: absolute;
    left: 0;
    width: 1180px;
    top: 128px;
    margin: 0;
    text-align: center;
    font-family: "Open Sans", "Segoe UI", sans-serif;
    font-weight: 400;
    font-size: 72px;
    line-height: 1;
    color: var(--ink);
  }
  .wordmark {
    position: absolute;
    left: 0;
    width: 1184px;
    top: 508px;
    margin: 0;
    text-align: center;
    font-family: "Archivo Black", "Arial Black", sans-serif;
    font-weight: 400;
    font-size: 106px;
    line-height: 1.2;
    letter-spacing: 3px;
    color: var(--wordmark);
    -webkit-text-stroke: 1px var(--wordmark-edge);
  }
  .varietal {
    position: absolute;
    left: 0;
    width: 1184px;
    top: 668px;
    margin: 0;
    text-align: center;
    font-family: "Abril Fatface", "Times New Roman", serif;
    font-weight: 400;
    font-size: 54px;
    line-height: 1.1;
    letter-spacing: 5px;
    color: var(--ink);
  }
  .vintage,
  .region,
  .origin {
    position: absolute;
    left: 0;
    width: 1180px;
    margin: 0;
    text-align: center;
    font-family: "Open Sans", "Segoe UI", sans-serif;
    font-weight: 400;
    color: var(--ink);
    line-height: 1;
  }
  .vintage { top: 731px; font-size: 49px; }
  .region  { top: 812px; font-size: 44px; }
  .origin  { top: 872px; font-size: 38px; }
</style>
</head>
<body>
<main class="label">
  <svg class="label-shape" width="1200" height="959" viewBox="0 0 1200 959">
    <defs>
      <radialGradient id="labelFill" cx="50%" cy="55%" r="65%">
        <stop offset="0%" stop-color="var(--label-light)"/>
        <stop offset="100%" stop-color="var(--label-edge)"/>
      </radialGradient>
      <radialGradient id="ornamentFillLeft" cx="0%" cy="0%" r="100%">
        <stop offset="0%" stop-color="var(--ornament)" stop-opacity="0.55"/>
        <stop offset="100%" stop-color="var(--ornament)" stop-opacity="0"/>
      </radialGradient>
      <radialGradient id="ornamentFillRight" cx="100%" cy="0%" r="100%">
        <stop offset="0%" stop-color="var(--ornament)" stop-opacity="0.55"/>
        <stop offset="100%" stop-color="var(--ornament)" stop-opacity="0"/>
      </radialGradient>
      <clipPath id="labelClip">
        <path d="M8 112 Q40 108 42 62 L300 62 Q590 -20 880 62 L1138 62 Q1140 108 1172 112 L1172 940 L8 940 Z"/>
      </clipPath>
    </defs>

    <path class="label-body" d="M8 112 Q40 108 42 62 L300 62 Q590 -20 880 62 L1138 62 Q1140 108 1172 112 L1172 940 L8 940 Z"
          fill="url(#labelFill)" stroke="var(--frame)" stroke-width="3"/>

    <g clip-path="url(#labelClip)">
      <rect class="corner-ornament" role="img" aria-label="Vine flourish with grape clusters, top left corner"
            x="8" y="20" width="340" height="290" fill="url(#ornamentFillLeft)"/>
      <rect class="corner-ornament" role="img" aria-label="Vine flourish with grape clusters, top right corner"
            x="832" y="20" width="340" height="290" fill="url(#ornamentFillRight)"/>
    </g>

    <line class="crest-rule" x1="360" y1="64" x2="820" y2="64" stroke="var(--frame)" stroke-width="3"/>
    <circle cx="590" cy="64" r="6" fill="var(--frame)"/>

    <ellipse class="landscape" role="img" aria-label="Photograph of the vineyard valley with mountains and river"
             cx="590" cy="390" rx="324" ry="126"
             fill="var(--scene-tone)" stroke="var(--frame)" stroke-width="4"/>
  </svg>

  <p class="brand-name-short">HC</p>

  <h1 class="wordmark">Harbor Crest</h1>
  <h2 class="varietal">PINOT GRIS</h2>
  <p class="vintage">2015</p>
  <p class="region">Waitaki Valley—North Otago</p>
  <p class="origin">New Zealand Wine</p>
</main>
</body>
</html>
```